indépendant en tant que Massothérapeute et Préparateur Mental, j'ai besoin de ...

Massothérapeute et préparateur mental indépendant, je recherche une carte de visite sobre et dynamique, sans images liées au massage ou à la préparation mentale mais intégrant mon logo. Les couleurs que j'aime bien sont : Blanc, gris, anthracite, noir et jaune

Contact Information for Business Card

carte de préférence Horizontale
neutre qui puisse toucher le deux domaines Massothérapie et préparation mentale

Requirements
Must have
• mon projet doit intégrer au recto:
LOGO
Loïc Vermande
078 315 26 49
info@loicvermande-exemple.ch
et éventuellement www.loicvermande-exemple.ch

et au verso les deux adresses:

Chemin des Ormelets 27B
1400 Yverdon-les-Bains

Rue des Tanneries 9
1700 Fribourg

Should not have
• mon projet ne doit pas contenir d'image en liens avec le massage ni la préparation mentale.

```html
<!DOCTYPE html>
<html lang="fr">
<head>
<meta charset="utf-8">
<title>Loïc Vermande – Carte de visite</title>
<link href="https://fonts.googleapis.com/css2?family=Open+Sans:wght@400;600&display=swap" rel="stylesheet">
<style>
  :root {
    --backdrop: #1f1f21;
    --paper: #ffffff;
    --anthracite: #2c2c2e;
    --ink: #262628;
    --steel: #98a4b1;
    --steel-dark: #7f8b98;
    --on-dark: #e9e9ea;
  }
  * { margin: 0; padding: 0; box-sizing: border-box; }
  html, body { width: 1200px; height: 900px; overflow: hidden; background: var(--backdrop); }
  body {
    display: flex; align-items: center; justify-content: center; gap: 60px;
    font-family: "Open Sans", Arial, sans-serif;
  }
  .card {
    position: relative; width: 520px; height: 336px; overflow: hidden;
  }
  .card--front { background: var(--paper); color: var(--ink); }
  .card--back { background: var(--anthracite); color: var(--on-dark); }

  .edge-tab {
    position: absolute; width: 10px; height: 78px; background: var(--steel);
  }
  .edge-tab::before, .edge-tab::after {
    content: ""; position: absolute; left: 0; width: 22px; height: 4px; background: var(--steel);
  }
  .edge-tab::before { top: 0; }
  .edge-tab::after { bottom: 0; }
  .edge-tab--left { left: 0; }
  .edge-tab--right { right: 0; }
  .edge-tab--right::before, .edge-tab--right::after { left: auto; right: 0; }
  .edge-tab--top { top: 0; }
  .edge-tab--bottom { bottom: 0; }
  .edge-tab--top::before { display: none; }
  .edge-tab--bottom::after { display: none; }

  .brand {
    position: absolute; left: 40px; top: 42px;
    display: flex; align-items: center; gap: 12px;
  }
  .brand__square { width: 30px; height: 30px; background: var(--ink); }
  .brand__name { font-size: 26px; font-weight: 600; color: var(--ink); letter-spacing: 0.2px; }
  .brand__role {
    position: absolute; left: 82px; top: 80px;
    font-size: 9px; font-weight: 600; letter-spacing: 0.8px; text-transform: uppercase; color: var(--ink);
  }

  .holder {
    position: absolute; left: 40px; bottom: 46px;
    font-size: 25px; font-weight: 400; line-height: 1.15; color: var(--ink);
  }

  .contact {
    position: absolute; left: 250px; top: 150px;
    display: flex; align-items: stretch; gap: 12px;
  }
  .contact__icons {
    width: 30px; border-radius: 5px; background: var(--steel);
    display: flex; flex-direction: column; justify-content: space-around; align-items: center; padding: 4px 0;
  }
  .contact__lines { display: flex; flex-direction: column; justify-content: space-around; gap: 10px; font-size: 14px; }
  .website {
    position: absolute; right: 36px; bottom: 46px; font-size: 14px; font-weight: 600;
  }

  .addresses {
    position: absolute; left: 44px; bottom: 52px;
    font-size: 15px; line-height: 1.4;
  }
  .address + .address { margin-top: 20px; }
</style>
</head>
<body>
  <section class="card card--front" aria-label="Recto">
    <span class="edge-tab edge-tab--right edge-tab--top"></span>
    <span class="edge-tab edge-tab--left edge-tab--bottom"></span>

    <div class="brand">
      <span class="brand__square"></span>
      <span class="brand__name">Loïc Vermande</span>
    </div>
    <p class="brand__role">Massothérapeute / Préparateur mental</p>

    <p class="holder">Loïc<br>Vermande</p>

    <div class="contact">
      <div class="contact__icons">
        <svg width="16" height="16" viewBox="0 0 24 24" aria-hidden="true"><path fill="#fff" d="M6.6 10.8a15 15 0 0 0 6.6 6.6l2.2-2.2c.3-.3.7-.4 1-.2 1.1.4 2.3.6 3.6.6.6 0 1 .4 1 1V20c0 .6-.4 1-1 1A17 17 0 0 1 3 4c0-.6.4-1 1-1h3.5c.6 0 1 .4 1 1 0 1.3.2 2.5.6 3.6.1.3 0 .7-.2 1z"/></svg>
        <svg width="16" height="16" viewBox="0 0 24 24" aria-hidden="true"><rect x="3" y="6" width="18" height="12" rx="1.5" fill="#fff"/><path d="M3.5 7l8.5 6 8.5-6" fill="none" stroke="#98a4b1" stroke-width="1.8"/></svg>
      </div>
      <div class="contact__lines">
        <span>078 315 26 49</span>
        <span>info@loicvermande-exemple.ch</span>
      </div>
    </div>

    <p class="website">www.loicvermande-exemple.ch</p>
  </section>

  <section class="card card--back" aria-label="Verso">
    <span class="edge-tab edge-tab--right edge-tab--top"></span>
    <span class="edge-tab edge-tab--left edge-tab--bottom"></span>

    <div class="addresses">
      <p class="address">Chemin des Ormelets 27B<br>1400 Yverdon-les-Bains</p>
      <p class="address">Rue des Tanneries 9<br>1700 Fribourg</p>
    </div>
  </section>
</body>
</html>
```